Web Design Project: Facility Management company

Hi! We need a new website.

Our current website: http://www.brantel-group.ru/ and we don-t like it. =)
The structure of our company has changed and now we don't need "cleaning" and "engeneering" on this site.

We are facility management company in Russia. So we provide integrated service solutions specific to industrial services: maintenance, repair, etc. of engineering systems.
More services:
Energy planning
Automation
Audit
Statements with regulators
Video surveillance
Central heating
Security systems
Welding
Management of subcontractors
Electrical installation and service needs
Reception
Catering

Visitors:
* Managers in the field of commercial real estate
* Chief engineers
* TOP managers of large companies, malls, factories...
+ their subordinates
* Small% of applicants.

Here you can see some websites/patterns we liked:
http://www.kvelmort.ru/ (This is our competitor’s site, so our site shouldn’t be an exact copy))))
http://www.orbitask.ru/
http://www.layoutpinery.com/demo/24296.html
http://www.layoutpinery.com/website-templates/10145.html

Style:
Light, hi-tech/minimalizm, the color palette should be based on the original site colors (Green + black + white). http://www.brantel-group.ru/

Estimated sitemap:
1. Home
2. About Us
3. Company's policy
4. History + Achievements.
5. Certificates
6. Map of presence (Here you can use sample map in file "our projects")
7. Services
8. Portfolio
9. News or blog
10. Jobs
11. Contacts - with the feedback form (or the function "call to order")
12. English

Need a design pages: main page, page 404. The rest of the page could be created by general pattern.

Logo, navigation bar and contacts should be visible on all pages of a site.
Flash animation elements and buttons, etc. - not needed.

* We need to develop 3 websites, so we are looking for a long term cooperation.
Looking forward to your creativity =)

Must Have:
Clear, intuitive structure of web pages.
In the center - of pictures reflecting our main services (industrial theme). May be in rotation.
BUT! This banner (central picture) should not be a huge one =)
All relevant information should be visible at once without scrolling.

A possibility to place media files (presentations, video ...) and 2 banner links on the main page.

Font should be available in Cyrillic.
Updates

IMPORTANT!

Please notice that in thisdesign we don't need "cleaning" and "engeneering" on this site.

So don't use old block of 4pictures from our current website. We don't need it anymore. 

Thestructure of our company has changed and now we need some links (may be banners,may be something else) to our future cleaning website as well as engeneeringwebsite.
It should look like seperate (partner) companies, not like our sevices.

Regards, Vera.

Please don't forget that we need bilingual site.

So define language changing tool in your designs.

Industry/Entity Type

Industrial

```html
<!DOCTYPE html>
<html lang="en">
<head>
<meta charset="utf-8">
<title>Brantel Service — Facility Management</title>
<link href="https://fonts.googleapis.com/css2?family=Didact+Gothic&family=Ubuntu:ital,wght@0,400;0,500;1,400&display=swap" rel="stylesheet">
<style>
:root{
  --green:#8dc63f;
  --green-dark:#5e9a16;
  --green-text:#5f9c1a;
  --ink:#222;
  --text:#333;
  --muted:#555;
  --line:#e2e2e2;
  --btn:#e4e4e4;
  --nav-top:#3a3a3a;
  --nav-bottom:#111;
  --white:#fff;
}
*{box-sizing:border-box;margin:0;padding:0}
html,body{width:890px;height:1200px;overflow:hidden;background:var(--white)}
body{font-family:"Ubuntu",sans-serif;color:var(--text);position:relative}
a{text-decoration:none;color:inherit}
.abs{position:absolute}
.heading{font-family:"Didact Gothic",sans-serif;color:var(--ink);font-weight:400}

.top-rule{left:0;top:0;width:890px;height:3px;background:#111}
.logo{left:16px;top:30px;width:217px;height:52px;background:#f4f6f2;display:flex;align-items:center;gap:9px;padding-left:10px}
.logo-mark{width:14px;height:14px;background:var(--green)}
.logo-name{font-weight:500;font-size:17px;letter-spacing:2px;color:var(--ink)}
.lang{left:392px;top:15px;font-size:10px;color:#999;display:flex;gap:4px}
.lang a{color:#444}
.lang a.current{color:var(--green-text);font-weight:500}
.search{left:445px;top:11px;width:163px;height:21px;border:1px solid #d6d6d6;font-size:9.5px;color:#777;padding:4px 7px}
.search::after{content:"";position:absolute;right:0;top:0;width:20px;height:19px;border-left:1px solid #d6d6d6}
.util-links{right:21px;top:14px;font-size:10.5px;color:#444}
.util-links span{padding:0 4px;color:#999}
.phone{left:706px;top:46px;display:flex;align-items:center;gap:7px}
.phone-num{font-size:17.5px;color:#333}

.nav{left:0;top:98px;width:890px;height:45px;background:linear-gradient(var(--nav-top),var(--nav-bottom));display:flex;justify-content:space-between;align-items:center;padding:0 40px 0 38px}
.nav a{color:var(--white);font-size:11.5px;font-weight:500}

.band{left:0;top:143px;width:890px;height:336px;background:var(--green)}
.slider{left:17px;top:153px;width:842px;height:314px;background:var(--white);border-radius:3px;box-shadow:0 1px 4px rgba(0,0,0,.25)}
.slide-photo{left:23px;top:158px;width:831px;height:244px;background:linear-gradient(100deg,#8c8c88 0%,#b9b6ac 30%,#d6b45a 45%,#c9c9c2 60%,#6b88a8 75%,#c8c6be 100%)}
.tabs{left:23px;top:402px;width:831px;height:61px;display:flex}
.tab{flex:1;display:flex;align-items:center;justify-content:center;text-align:center;font-size:12.5px;line-height:19px;color:#333;background:linear-gradient(#fff,#e8e8e8);border-right:1px solid #c9c9c9;font-family:"Didact Gothic",sans-serif}
.tab:last-child{border-right:0}
.tab.active{background:linear-gradient(var(--green),var(--green-dark));color:var(--white);position:relative}
.tab.active::before{content:"";position:absolute;top:-7px;left:50%;margin-left:-7px;border:7px solid transparent;border-top:0;border-bottom-color:var(--green)}

.welcome{left:17px;top:494px;width:549px;height:253px;border:4px solid #ececec;padding:14px 14px}
.welcome h1{font-size:19px;margin-bottom:8px}
.lead{font-size:11.5px;line-height:16px;color:#222;margin-bottom:9px;text-align:justify}
.body-copy{font-size:9.6px;line-height:15.6px;color:var(--muted);text-align:justify;margin-bottom:8px}
.btn{display:inline-block;background:var(--btn);color:#333;font-size:10px;padding:5px 12px;border-radius:2px;box-shadow:0 1px 0 #c8c8c8}

.services{left:582px;top:500px;width:290px}
.services h2{font-size:17px;margin-bottom:4px}
.arrow-list{list-style:none}
.arrow-list li{font-size:10.3px;line-height:23.5px;color:#333;padding-left:13px;position:relative}
.arrow-list li::before{content:"";position:absolute;left:1px;top:9px;border:3px solid transparent;border-left:4px solid #666;border-right:0}

.col-title{font-size:15.5px;top:780px}
.divider{top:782px;width:1px;height:274px;background:var(--line)}
.tech-frame{left:13px;top:810px;width:251px;height:108px;background:#fff;box-shadow:0 1px 4px rgba(0,0,0,.2)}
.tech-photo{left:18px;top:815px;width:242px;height:98px;background:linear-gradient(90deg,#c7d8ea,#e6eef6 45%,#5c6f86 70%,#d9e4ef)}
.green-lead{font-size:11px;line-height:15.6px;color:var(--green-text)}
.col-copy{font-size:10.2px;line-height:15.6px;color:#333;text-align:justify}
.tick-list{list-style:none}
.tick-list li{font-size:10.4px;line-height:24.3px;display:flex;align-items:center;gap:9px}
.tick{width:13px;height:13px;border-radius:50%;background:var(--green);position:relative;flex:none}
.tick::after{content:"";position:absolute;left:5px;top:3.5px;border:3px solid transparent;border-left:4px solid #fff;border-right:0}
.blog-date{font-size:10px;color:var(--green-text);margin-bottom:2px}
.blog-text{font-size:9.8px;line-height:15.6px;font-style:italic;color:#333;text-align:justify;margin-bottom:6px}

.footer{left:0;top:1113px;width:890px;height:87px;background:linear-gradient(#3a3a3a,#0e0e0e)}
.footer-links{left:18px;top:1128px;font-size:10.4px;color:#fff;white-space:nowrap}
.footer-note{left:18px;top:1152px;font-size:8px;color:#aaa}
</style>
</head>
<body>
<div class="abs top-rule"></div>

<div class="abs logo"><span class="logo-mark"></span><span class="logo-name">BRANTEL SERVICE</span></div>
<div class="abs lang"><a class="current" href="#">EN</a>|<a href="#">RU</a></div>
<div class="abs search">enter keyword</div>
<div class="abs util-links">Company<span>|</span>Chosen by<span>|</span>Our team<span>|</span>Contact Us</div>
<div class="abs phone">
  <svg width="26" height="26" viewBox="0 0 26 26" aria-hidden="true">
    <circle cx="13" cy="13" r="12.5" fill="#8dc63f"/>
    <path d="M9 6.5c1 0 2 2.6 2 3.2 0 .8-1.3 1.2-1.1 2 .5 1.6 2.1 3.3 3.6 3.9.8.3 1.2-1 2-1 .6 0 3.2 1 3.2 2 0 1.3-1.6 2.4-2.8 2.4-4.4 0-8.8-4.6-8.8-9 0-1.3 1-3.5 1.9-3.5z" fill="#fff"/>
  </svg>
  <span class="phone-num">+7 812 555 0142</span>
</div>

<nav class="abs nav">
  <a href="#">HOME</a><a href="#">ABOUT US</a><a href="#">COMPANY'S POLICY</a><a href="#">HISTORY</a><a href="#">CERTIFICATES</a><a href="#">LOCATIONS MAP</a><a href="#">SERVICES</a><a href="#">PORTFOLIO</a><a href="#">BLOG</a><a href="#">JOBS</a>
</nav>

<div class="abs band"></div>
<div class="abs slider"></div>
<div class="abs slide-photo" role="img" aria-label="Two engineers in orange hard hats in front of a concrete wall and yellow scaffolding"></div>
<div class="abs tabs">
  <div class="tab active">Integrated<br>Facility</div>
  <div class="tab">Energy Planning &amp; Audit</div>
  <div class="tab">Automation &amp; Security</div>
  <div class="tab">Central Heating &amp;<br>Electrical Installation</div>
</div>

<section class="abs welcome">
  <h1 class="heading">Welcome to Our Company!</h1>
  <p class="lead">Pellentesque faucibus. Ut accumsan ultricies elit. Maecenas at justo id velit placerat molestie. Donec dictum lectus non odio. Cras a ante vitae enim iaculis aliquam.</p>
  <p class="body-copy">Mauris nunc quam, venenatis nec, euismod sit amet, egestas placerat, est. Pellentesque habitant morbi tristique senectus et netus et malesuada fames ac turpis egestas. Cras id elit. Integer quis urna. Ut ante enim, dapibus malesuada, fringilla eu, condimentum quis, tellus. Aenean porttitor eros vel dolor. Donec convallis pede venenatis nibh. Duis quam. Nam eget lacus. Aliquam erat volutpat. Quisque dignissim congue leo.</p>
  <p class="body-copy">Mauris vel lacus vitae felis vestibulum volutpat. Etiam est nunc, venenatis in, tristique eu, imperdiet ac, nisl. Cum sociis natoque penatibus et magnis dis parturient montes, nascetur ridiculus mus. In iaculis facilisis massa. Etiam eu urna. Sed porta. Suspendisse quam leo, molestie sed, luctus quis, feugiat in, pede.</p>
  <a class="btn" href="#">read more</a>
</section>

<section class="abs services">
  <h2 class="heading">What Can We Do</h2>
  <ul class="arrow-list">
    <li>Commercial property management</li>
    <li>Maintenance of immovable property</li>
    <li>Maintenance of dangerous industrial objects</li>
    <li>Energy planning, automation and audit</li>
    <li>Video surveillance &amp; security systems</li>
    <li>Central heating, welding and electrical service</li>
    <li>Outsourcing &amp; staff leasing</li>
    <li>Work with oversight bodies and government services</li>
  </ul>
  <a class="btn" href="#" style="margin-top:9px;margin-left:2px">read more</a>
</section>

<div class="abs divider" style="left:282px"></div>
<div class="abs divider" style="left:577px"></div>

<h2 class="abs heading col-title" style="left:18px">Our Technology</h2>
<div class="abs tech-frame"></div>
<div class="abs tech-photo" role="img" aria-label="Two business people in yellow hard hats at a construction site"></div>
<div class="abs" style="left:17px;top:928px;width:248px">
  <p class="green-lead">Mauris vel lacus vitae felis vestibulum volutpat. Etiam est nunc, venenatis in,</p>
  <p class="col-copy" style="margin-top:4px">Nulla rhoncus dictum metus. Curabitur tristique mi condimentum orci. Phasellus pellentesque aliquam enim. Proin dui lectus, cursus eu, mattis laoreet, viverra sit amet, quam. Curabitur vel dolor ultrices ipsum dictum tristique. Praesent vitae lacus.</p>
</div>
<a class="abs btn" href="#" style="left:17px;top:1060px">learn more</a>

<h2 class="abs heading col-title" style="left:297px">Why do they choose Us?</h2>
<div class="abs" style="left:299px;top:808px;width:262px">
  <p class="col-copy">Following the complex approach to management problems, we will help to optimize maintenance costs and your immovable property service.</p>
  <p class="col-copy" style="margin-top:8px">We use an accumulated experience of immovable property maintenance, any kind of engineering systems, and their modernization for extension of durability time, and you save your money.</p>
  <ul class="tick-list" style="margin-top:6px">
    <li><span class="tick"></span>Maintenance of dangerous industrial objects</li>
    <li><span class="tick"></span>Technical service of engineering systems</li>
    <li><span class="tick"></span>Management of subcontractors</li>
    <li><span class="tick"></span>Work with oversight bodies and government</li>
  </ul>
</div>
<a class="abs btn" href="#" style="left:305px;top:1060px">learn more</a>

<h2 class="abs heading col-title" style="left:594px">Recent Blog</h2>
<div class="abs" style="left:595px;top:810px;width:270px">
  <p class="blog-date">20.Aug.2012</p>
  <p class="blog-text">Donec convallis pede venenatis nibh. Duis quam. Nam eget lacus. Aliquam erat volutpat. Quisque dignissim congue leo.</p>
  <p class="blog-date">10.Aug.2012</p>
  <p class="blog-text" style="margin-bottom:1px">Mauris vel lacus vitae felis vestibulum volutpat. Etiam est nunc, venenatis in, tristique eu, imperdiet ac, nisl.</p>
  <p class="blog-text" style="margin-bottom:14px">Cum sociis natoque penatibus et magnis dis parturient montes, nascetur ridiculus mus. In iaculis facilisis massa. Etiam eu urna. Sed porta.</p>
  <p class="blog-date">10.Aug.2012</p>
  <p class="blog-text">Cum sociis natoque penatibus et magnis dis parturient montes, nascetur ridiculus mus. In iaculis facilisis massa. Etiam eu urna. Sed porta.</p>
</div>
<a class="abs btn" href="#" style="left:593px;top:1059px">View more</a>

<footer class="abs footer"></footer>
<div class="abs footer-links">Company | Chosen by | Our team | Contact us | Integrated facility management | Energy planning | Automation | Partners: Brantel Clean | Brantel Engineering</div>
<div class="abs footer-note">© 2012 Company Name &nbsp;| &nbsp;All right reserved &nbsp;| &nbsp;Policy privacy</div>
</body>
</html>
```